Sneaker Company looking for a partner on multiple packaging designs!

We are a company who is passionate about Sneakers and quality products! This project is the first of many packaging designs we will need. We have our logo (see attached) and we would like the background to be all black for this package. I'm working on the UPC number right now so please leave a space for the UPC. Where we need some help is the overall design and some "marketing" word smithing. We are hoping to find a partner that we can work with on future products as well who really understands us and our products! Our company name is Trodo and this first product will be for crease protection. They are known at Crease Guards, Crease Protection, Anti-Crease Inserts, etc...Not sure the right name to go with but would love some feedback! The package will have 2 Pairs inside. (One Black and One white). This product is something you slide into the shoe while you are wearing it. This product helps prevent the creasing of the toe box. Basically to help keep the sneaker clean and crisp! They are labeled L and R for Left and Right. They are also thin enough that you can trim them with scissors to fit! I have much more to share but before adding all the marketing words, if this is a project you would like to take on please message me and let’s chat! I want to make sure this is a good fit for both of us. Please do not submit projects without speaking to me first. If doing so that means you didn’t read this and you will immediately be removed from contention.

Thank you and look forward to working with you!
Marcus

Target Market(s)

Customers who love Sneakers

Industry/Entity Type

Retail

Font styles to use
Sans Serif

Requirements
Must have
• Clean, Original and Simple
Nice to have
• Pretty open!
Should not have
• Anything copied from another product. No more than 4 colors total on the box.

```html
<!DOCTYPE html>
<html lang="en">
<head>
<meta charset="utf-8">
<title>Trodo — Crease Guard Box Dieline</title>
<link rel="stylesheet" href="https://fonts.googleapis.com/css2?family=Quicksand:wght@500;600&display=swap">
<style>
  :root {
    --paper: #ffffff;
    --board: #231f20;
    --art-dark: #141416;
    --art-mid: #1d1d1f;
    --art-green: #0f5a34;
    --fold: #d9d9d9;
    --brand-grey: #6b6b6e;
    --brand-green: #35c08e;
    --copy: #cfcfcf;
  }
  html, body {
    margin: 0;
    padding: 0;
    width: 1116px;
    height: 1200px;
    overflow: hidden;
    background: var(--paper);
  }
  .dieline {
    display: block;
    width: 1116px;
    height: 1200px;
  }
  .board { fill: var(--board); stroke: var(--fold); stroke-width: 1.5; }
  .brand-name {
    font-family: "Quicksand", sans-serif;
    font-weight: 600;
    fill: var(--brand-grey);
    letter-spacing: 4px;
  }
  .brand-mark { fill: var(--brand-green); }
  .body-copy {
    font-family: "Quicksand", sans-serif;
    font-weight: 500;
    font-size: 17px;
    fill: var(--copy);
  }
</style>
</head>
<body>
<svg class="dieline" viewBox="0 0 1500 1613" xmlns="http://www.w3.org/2000/svg">
  <defs>
    <linearGradient id="face-tone-front" x1="0" y1="0" x2="1" y2="1">
      <stop offset="0" stop-color="var(--art-mid)"/>
      <stop offset="0.55" stop-color="var(--art-dark)"/>
      <stop offset="1" stop-color="var(--art-green)"/>
    </linearGradient>
    <linearGradient id="face-tone-back" x1="1" y1="0" x2="0" y2="1">
      <stop offset="0" stop-color="var(--art-mid)"/>
      <stop offset="0.55" stop-color="var(--art-dark)"/>
      <stop offset="1" stop-color="var(--art-green)"/>
    </linearGradient>
  </defs>

  <!-- Top: glue strip, side panel, front face -->
  <rect class="board" x="181" y="170" width="40" height="431"/>
  <rect class="board" x="221" y="170" width="186" height="431"/>
  <rect x="408" y="170" width="660" height="431" fill="url(#face-tone-front)"
        role="img" aria-label="Abstract dark metallic artwork with green and silver angled bands"/>
  <g transform="translate(300 385) rotate(90)">
    <text class="brand-name" x="0" y="0" font-size="46" text-anchor="middle" dominant-baseline="middle">trodo</text>
    <rect class="brand-mark" x="78" y="-9" width="18" height="18"/>
  </g>
  <text class="brand-name" x="980" y="565" font-size="88" text-anchor="end">trodo</text>
  <rect class="brand-mark" x="992" y="528" width="26" height="26"/>

  <!-- Middle band: flaps and top panel -->
  <rect class="board" x="243" y="603" width="163" height="184"/>
  <rect class="board" x="408" y="603" width="660" height="184"/>
  <rect class="board" x="1068" y="603" width="162" height="184"/>
  <text class="brand-name" x="984" y="737" font-size="46" text-anchor="end">trodo</text>
  <rect class="brand-mark" x="992" y="719" width="16" height="16"/>

  <!-- Lower: back face, side panel, glue strip -->
  <rect x="408" y="789" width="660" height="431" fill="url(#face-tone-back)"
        role="img" aria-label="Abstract dark metallic artwork with green and silver angled bands"/>
  <rect class="board" x="1068" y="789" width="184" height="431"/>
  <rect class="board" x="1254" y="789" width="39" height="431"/>
  <g transform="translate(1170 1005) rotate(-90)">
    <text class="brand-name" x="0" y="0" font-size="46" text-anchor="middle" dominant-baseline="middle">trodo</text>
    <rect class="brand-mark" x="78" y="-9" width="18" height="18"/>
  </g>
  <text class="body-copy" text-anchor="end">
    <tspan x="1037" y="838">Lorem ipsum dolor sit amet, consectetuer adipiscing</tspan>
    <tspan x="1037" y="859">elit, sed diam nonummy nibh euismod tincidunt ut</tspan>
    <tspan x="1037" y="880">laoreet dolore magna aliquam erat volutpat. Ut wisi</tspan>
    <tspan x="1037" y="901">enim ad minim veniam, quis nostrud exerci tation</tspan>
    <tspan x="1037" y="922">ullamcorper suscipit lobortis nisl ut aliquip ex ea</tspan>
    <tspan x="1037" y="943">commodo consequat. Duis autem vel eum iriure</tspan>
    <tspan x="1037" y="964">dolor in hendrerit in vulputate</tspan>
  </text>
  <text class="brand-name" x="460" y="1188" font-size="88">trodo</text>
  <rect class="brand-mark" x="718" y="1152" width="26" height="26"/>

  <!-- Bottom band: flaps, base panel, tuck strip -->
  <rect class="board" x="243" y="1222" width="163" height="183"/>
  <rect class="board" x="408" y="1222" width="660" height="183"/>
  <rect class="board" x="1068" y="1222" width="162" height="183"/>
  <text class="brand-name" x="444" y="1346" font-size="46">trodo</text>
  <rect class="brand-mark" x="594" y="1328" width="16" height="16"/>
  <rect class="board" x="408" y="1407" width="658" height="39"/>
</svg>
</body>
</html>
```